Team email banner for internal communications

We need a team email banner/header that will be applied to all internal communications from our department to other functions. The graphic should be optimized for Outlook and be landscape in layout. We have 5 different silo within our team and will need so will either need have a blank space to denote each team or have change in colors/graphics to denote each team (see current headers attached to job description). We are looking for a banner that combines our team logo (attached) with our team name, Regional Talent & Coaching Unit. The theme should be L&D and pharmaceutical in nature.

Need extra days to review

The text in the banner should be Regional Talent & Coaching Unit with the team logo (attached).

```html
<!DOCTYPE html>
<html lang="en">
<head>
<meta charset="utf-8">
<title>Regional Talent &amp; Coaching Unit – Hematology Email Banner</title>
<link rel="stylesheet" href="https://fonts.googleapis.com/css2?family=Montserrat:wght@600;700;800&display=swap">
<style>
  :root {
    --brand-red: #da2d28;
    --ink-black: #231f20;
    --paper-white: #ffffff;
    --stage-grey: #c5c9d0;
    --photo-mist: #dde3e8;
    --photo-steel: #b9c3cb;
    --photo-glove: #eef1f4;
    --photo-blood: #5a1418;
  }
  * { margin: 0; padding: 0; box-sizing: border-box; }
  html, body {
    width: 1200px;
    height: 666px;
    overflow: hidden;
    background: var(--stage-grey);
  }
  .canvas {
    position: relative;
    width: 1200px;
    height: 666px;
  }
  .banner {
    position: absolute;
    left: 40px;
    top: 127px;
    width: 1120px;
    height: 412px;
    overflow: hidden;
    font-family: "Montserrat", sans-serif;
  }
  .banner-shapes {
    position: absolute;
    inset: 0;
    width: 100%;
    height: 100%;
  }
  .company-mark {
    position: absolute;
    left: 94px;
    top: 15px;
    display: flex;
    align-items: center;
    gap: 12px;
  }
  .company-mark-square {
    width: 45px;
    height: 45px;
    border-radius: 8px;
    background: var(--brand-red);
  }
  .company-name {
    font-size: 34px;
    font-weight: 700;
    color: var(--ink-black);
    letter-spacing: -0.5px;
  }
  .team-title {
    position: absolute;
    left: 190px;
    top: 190px;
    font-size: 40px;
    font-weight: 700;
    line-height: 1;
    color: var(--ink-black);
    letter-spacing: 0.5px;
    white-space: nowrap;
  }
  .team-rule {
    position: absolute;
    left: 248px;
    top: 240px;
    width: 202px;
    height: 3px;
    background: var(--ink-black);
  }
  .team-subtitle {
    position: absolute;
    left: 458px;
    top: 233px;
    font-size: 15px;
    font-weight: 700;
    line-height: 1;
    color: var(--paper-white);
    letter-spacing: 2.4px;
    white-space: nowrap;
  }
  .silo-name {
    position: absolute;
    left: 88px;
    top: 346px;
    font-size: 38px;
    font-weight: 800;
    line-height: 1;
    color: var(--ink-black);
    letter-spacing: 0.5px;
  }
</style>
</head>
<body>
<div class="canvas">
  <section class="banner">
    <svg class="banner-shapes" viewBox="0 0 2224 819" preserveAspectRatio="none" aria-hidden="false">
      <defs>
        <linearGradient id="lab-backdrop" x1="0" y1="0" x2="1" y2="1">
          <stop offset="0" stop-color="var(--paper-white)"/>
          <stop offset="0.55" stop-color="var(--photo-mist)"/>
          <stop offset="1" stop-color="var(--photo-steel)"/>
        </linearGradient>
        <radialGradient id="sample-photo" cx="0.55" cy="0.5" r="0.6">
          <stop offset="0" stop-color="var(--photo-blood)"/>
          <stop offset="0.35" stop-color="#9a6f78"/>
          <stop offset="0.6" stop-color="var(--photo-glove)"/>
          <stop offset="1" stop-color="var(--photo-mist)"/>
        </radialGradient>
      </defs>

      <rect class="lab-backdrop" x="0" y="0" width="2224" height="819" fill="url(#lab-backdrop)"
            role="img" aria-label="Soft-focus laboratory photograph"/>

      <polygon class="corner-red" points="1576,0 2224,0 2224,819" fill="var(--brand-red)"/>
      <polygon class="diagonal-black" points="988,0 1576,0 2224,819 1628,819 1456,597" fill="var(--ink-black)"/>

      <path class="title-band" d="M0,141 H1100 Q1180,141 1230,205 L1445,465 Q1495,530 1445,595 L1306,819 H0 Z"
            fill="var(--brand-red)"/>
      <path class="silo-panel" d="M0,627 H1070 Q1130,627 1170,668 L1306,819 H0 Z" fill="var(--paper-white)"/>
      <polygon class="lab-glimpse" points="1306,819 1628,819 1456,597" fill="var(--photo-steel)"
               role="img" aria-label="Glimpse of laboratory photograph"/>

      <circle class="photo-frame" cx="1841" cy="387" r="323" fill="var(--paper-white)"/>
      <circle class="sample-photo" cx="1841" cy="387" r="287" fill="url(#sample-photo)"
              role="img" aria-label="Photo of a gloved hand holding two blood sample tubes"/>

      <circle class="team-mark" cx="240" cy="365" r="95" fill="var(--paper-white)"/>
    </svg>

    <div class="company-mark">
      <span class="company-mark-square"></span>
      <span class="company-name">Norvale Bio</span>
    </div>

    <h1 class="team-title">REGIONAL TALENT</h1>
    <span class="team-rule"></span>
    <p class="team-subtitle">&amp; COACHING UNIT</p>

    <h2 class="silo-name">HEMATALOGY</h2>
  </section>
</div>
</body>
</html>
```